Do i have coronavirus, flue or cold?

Using information from QRV and government agencies we want to make a easy to read infographic helping patients see if they have coronavirus, the flu or a cold. Using a flow diagram or whatever you think will make it easy to read and digest for the average lamen.

Information is in the word document and in the chart.

We are www.tovipharm.co.uk attached is our brand guidelines, we will be putting this infographic on our website and email/sms it to all of our 300,000 patients.

```html
<!DOCTYPE html>
<html lang="en">
<head>
<meta charset="utf-8">
<title>Do I have Coronavirus, the Flu or a Cold?</title>
<link href="https://fonts.googleapis.com/css2?family=Oswald:wght@500;600&family=Roboto:ital,wght@0,500;0,700;1,700&display=swap" rel="stylesheet">
<style>
  :root{
    --navy:#3f4a9e;
    --navy-dark:#121845;
    --orange:#f15a22;
    --salmon:#f6a07e;
    --pale:#eef7fa;
    --head-tint:#d3dcee;
    --white:#ffffff;
    --skin:#f2b27f;
    --shirt:#7b8bd0;
  }
  *{margin:0;padding:0;box-sizing:border-box}
  html,body{width:1200px;height:2431px;overflow:hidden;background:var(--white)}
  body{position:relative;font-family:'Roboto',Arial,sans-serif}

  .title-band{position:absolute;left:0;top:0;width:1168px;height:120px;background:var(--navy);
    display:flex;align-items:center;justify-content:center}
  .title-band h1{font-family:'Oswald',Impact,sans-serif;font-weight:600;font-size:58px;color:var(--white);letter-spacing:1px}

  .col-heads{position:absolute;top:127px;left:14px;display:grid;grid-template-columns:376px 261px 247px 259px;height:94px}
  .col-heads div{display:flex;align-items:center;justify-content:center;font-weight:500;color:var(--navy);font-size:33px}
  .col-heads .symptom-head{font-size:32px;justify-content:flex-start;padding-left:118px}
  .col-heads .tint{background:var(--head-tint)}

  .chart{position:absolute;top:228px;left:14px;display:grid;
    grid-template-columns:370px 6px 261px 247px 259px;grid-auto-rows:196px}

  .symptom{position:relative;overflow:hidden;background:var(--pale);border-bottom:2px solid var(--white)}
  .symptom.accent{background:var(--salmon)}
  .art{position:absolute;z-index:0;left:40px;top:14px;width:120px;height:170px;border-radius:12px;
    background:linear-gradient(170deg,var(--skin) 0 30%,var(--shirt) 60%,var(--navy))}
  .accent .art{left:70px;top:8px;width:178px;height:178px;border-radius:50%;
    background:radial-gradient(circle at 50% 50%,var(--shirt) 0 50%,var(--white) 51%)}
  .art.fever{left:40px}
  .art.tired{left:30px;top:40px;width:150px;height:140px}
  .art.muscle{left:90px}
  .art.throat{left:105px;width:105px}
  .art.sneeze{left:80px;width:110px}
  .art.breath{left:4px;width:168px;height:168px;top:14px}
  .art.head{left:12px}
  .art.nose{left:18px}

  .label{position:absolute;z-index:1;right:30px;top:46px;text-align:right;font-family:'Oswald',Impact,sans-serif;
    font-weight:500;font-size:38px;line-height:44px;color:var(--orange);text-transform:uppercase;white-space:nowrap}
  .accent .label{color:var(--white);right:12px}
  .label.cough{top:22px}
  .label.tired{right:12px}
  .label.breath{top:48px;text-align:left;right:auto;left:188px;font-size:37px}
  .label.muscle{top:50px;right:40px;text-align:center}
  .label.head{top:34px}
  .label.throat{top:42px}
  .label.nose{top:30px;right:30px}
  .label.sneeze{top:34px;right:20px}

  .spacer{background:var(--white)}
  .cell{display:flex;flex-direction:column;align-items:center;justify-content:center;
    border-top:3px dotted var(--navy);border-right:3px solid var(--navy);background:var(--pale);
    font-weight:700;color:var(--navy);font-size:30px}
  .cell.first{border-left:3px solid var(--navy)}
  .cell.yes{background:var(--white)}
  .cell.last-row{border-bottom:3px dotted var(--navy)}
  .yes-mark{font-family:'Oswald',Impact,sans-serif;font-weight:600;font-size:74px;line-height:80px;color:var(--orange)}
  .note{font-style:italic;font-size:30px;color:var(--navy)}

  .symptoms-band{position:absolute;left:17px;top:2012px;width:1150px;height:70px;
    background:linear-gradient(90deg,var(--orange) 0%,#f3823f 55%,rgba(255,255,255,0) 85%)}
  .symptoms-band h2{font-weight:500;font-size:34px;color:var(--white);line-height:70px;padding-left:72px;letter-spacing:.5px}
  .summary{position:absolute;left:55px;top:2104px;width:760px;font-weight:500;font-size:23.5px;line-height:31.5px;color:var(--orange)}
  .virus-art{position:absolute;left:820px;top:2040px;width:350px;height:240px;
    background:radial-gradient(circle at 55% 40%,#e8963a 0 18%,rgba(245,190,120,.5) 30%,rgba(255,255,255,0) 60%)}

  .footer{position:absolute;left:0;top:2303px;width:1168px;height:128px;background:var(--navy-dark);color:var(--white);text-align:center}
  .credit{display:flex;align-items:center;justify-content:center;gap:20px;margin-top:22px;font-style:italic;font-weight:700;font-size:25px}
  .brand{display:flex;align-items:center;gap:10px;font-style:italic;font-weight:700;font-size:28px}
  .brand i{display:block;width:34px;height:34px;border-radius:50%;background:var(--head-tint)}
  .source{margin-top:18px;font-style:italic;font-weight:700;font-size:21px}
</style>
</head>
<body>
  <header class="title-band"><h1>Do I have Coronavirus, the Flu or a Cold ?</h1></header>

  <div class="col-heads">
    <div class="symptom-head">Symptom</div>
    <div class="tint">CORONAVIRUS</div>
    <div>FLU</div>
    <div class="tint">COLD</div>
  </div>

  <main class="chart">
    <div class="symptom"><div class="art fever" role="img" aria-label="Illustration of a person with a fever taking their temperature"></div><div class="label">Fever</div></div>
    <div class="spacer"></div>
    <div class="cell yes first"><span class="yes-mark">Yes</span></div>
    <div class="cell yes"><span class="yes-mark">Yes</span><span class="note">High</span></div>
    <div class="cell">Rare</div>

    <div class="symptom accent"><div class="art" role="img" aria-label="Illustration of a person coughing"></div><div class="label cough">Cough</div></div>
    <div class="spacer"></div>
    <div class="cell yes first"><span class="yes-mark">Yes</span></div>
    <div class="cell yes"><span class="yes-mark">Yes</span></div>
    <div class="cell">Moderate</div>

    <div class="symptom"><div class="art tired" role="img" aria-label="Illustration of a tired person sleeping under a blanket"></div><div class="label tired">Tiredness</div></div>
    <div class="spacer"></div>
    <div class="cell yes first"><span class="yes-mark">Yes</span></div>
    <div class="cell yes"><span class="yes-mark">Yes</span></div>
    <div class="cell">Mild</div>

    <div class="symptom accent"><div class="art breath" role="img" aria-label="Illustration of a person short of breath"></div><div class="label breath">Shortness<br>of breath</div></div>
    <div class="spacer"></div>
    <div class="cell yes first"><span class="yes-mark">Yes</span></div>
    <div class="cell yes"><span class="yes-mark">Yes</span></div>
    <div class="cell">Rare</div>

    <div class="symptom"><div class="art muscle" role="img" aria-label="Illustration of a person with aching muscles"></div><div class="label muscle">Muscle<br>ache</div></div>
    <div class="spacer"></div>
    <div class="cell yes first"><span class="yes-mark">Yes</span></div>
    <div class="cell yes"><span class="yes-mark">Yes</span><span class="note">Often</span></div>
    <div class="cell">Moderate</div>

    <div class="symptom accent"><div class="art head" role="img" aria-label="Illustration of a person holding their head with a headache"></div><div class="label head">Headache</div></div>
    <div class="spacer"></div>
    <div class="cell first">Sometimes</div>
    <div class="cell yes"><span class="yes-mark">Yes</span></div>
    <div class="cell">Rare</div>

    <div class="symptom"><div class="art throat" role="img" aria-label="Illustration of a person with a scarf and sore throat"></div><div class="label throat">Sore<br>throat</div></div>
    <div class="spacer"></div>
    <div class="cell first">Sometimes</div>
    <div class="cell">Sometimes</div>
    <div class="cell yes"><span class="yes-mark">Yes</span></div>

    <div class="symptom accent"><div class="art nose" role="img" aria-label="Illustration of a person blowing a runny nose"></div><div class="label nose">Stuffy/<br>runny<br>nose</div></div>
    <div class="spacer"></div>
    <div class="cell first">Rare</div>
    <div class="cell">Sometimes</div>
    <div class="cell yes"><span class="yes-mark">Yes</span></div>

    <div class="symptom"><div class="art sneeze" role="img" aria-label="Illustration of a person sneezing into a tissue"></div><div class="label sneeze">Sneezing</div></div>
    <div class="spacer"></div>
    <div class="cell first last-row">No</div>
    <div class="cell last-row">Sometimes</div>
    <div class="cell yes last-row"><span class="yes-mark">Yes</span></div>
  </main>

  <section>
    <div class="symptoms-band"><h2>CORONAVIRUS &nbsp;SYMPTOMS</h2></div>
    <p class="summary">The most common symptoms of COVID-19 are fever, tiredness,<br>and dry cough. Some patients may have aches and pains, nasal<br>congestion, runny nose, sore throat or diarrhoea. These symptoms<br>are usually mild and begin gradually. Some people become<br>infected but don’t develop any symptoms and don't feel unwell.</p>
    <div class="virus-art" role="img" aria-label="Illustration of orange virus particles"></div>
  </section>

  <footer class="footer">
    <div class="credit">Brought to you by: <span class="brand"><i></i>Tovipharm</span></div>
    <p class="source">Source: QRV, National Health Protection Agency</p>
  </footer>
</body>
</html>
```